Mar-wick Sky Harbor Custom Brokers Limited

The Company deals with:
shipping
logistic
imports
Export
customs clearance (customs broker services); and
customers can shop online and we take care of the shipment from the United States of America to Jamaica.
(we offer freight forwarding services from USA to Kingston Jamaica
Our tagline is : Creating Waves in the Logistic Industry.
Address: Shop 9 Birchfield Trade Centre, 227-229 Welland Avenue Kingston 8, Jamaica West Indies Telephone: (876)555-0193
Example of what we required can be seem: www.swiftparcelhubexample.com

```html
<!DOCTYPE html>
<html lang="en">
<head>
<meta charset="utf-8">
<title>Mar-wick Sky Harbor Custom Brokers Limited</title>
<link rel="stylesheet" href="https://fonts.googleapis.com/css2?family=Poppins:wght@400;500;600;700;800&family=Roboto:wght@400;500&display=swap">
<style>
:root{
  --navy:#0f3a6e;
  --navy-deep:#0b2d57;
  --gold:#e9a800;
  --ink:#222;
  --muted:#555;
  --light:#f3f3f3;
  --white:#fff;
}
*{margin:0;padding:0;box-sizing:border-box}
html,body{width:1200px;height:4330px;overflow:hidden}
body{position:relative;background:var(--white);font-family:"Poppins",sans-serif;color:var(--ink)}
.abs{position:absolute}
.brand{display:flex;align-items:center;gap:8px;font-weight:700;color:var(--navy);font-size:13px;letter-spacing:.5px;white-space:nowrap}
.brand-dot{width:22px;height:22px;border-radius:50%;background:var(--gold)}
.social{display:flex;gap:12px;font-size:11px;color:#666;font-family:"Roboto",sans-serif;white-space:nowrap}
.nav{top:70px;left:0;width:1200px;height:42px;background:var(--navy);}
.nav ul{list-style:none;display:flex;position:absolute;left:88px;top:0;height:42px}
.nav li{color:#fff;font-size:11.5px;font-weight:600;padding:0 19px;line-height:42px;white-space:nowrap}
.nav li.active{background:var(--gold);padding:0 22px}
.hero{top:112px;left:0;width:1200px;height:830px;overflow:hidden}
.hero-photo{position:absolute;inset:0;background:linear-gradient(100deg,#0f3a6e 0%,#1d4f86 35%,#8e8a7a 60%,#c9b27a 75%,#e5e5e5 100%)}
.hero-kicker{left:90px;top:262px;color:#fff;font-size:24px;font-weight:600;letter-spacing:.5px;white-space:nowrap}
.hero-title{left:84px;top:290px;color:#fff;font-size:70px;font-weight:800;line-height:70px;letter-spacing:1px;white-space:nowrap}
.arrow{width:32px;height:68px;background:rgba(0,0,0,.35);color:#fff;font-size:14px;display:flex;align-items:center;justify-content:center}
h2.sec{font-size:36px;font-weight:700;color:var(--ink);letter-spacing:.5px;line-height:1.05}
.center{text-align:center;left:0;width:1200px}
p.body{font-family:"Roboto",sans-serif;font-size:15.5px;line-height:26px;color:var(--muted)}
.btn-slant{height:34px;background:var(--gold);color:#fff;font-size:11px;font-weight:700;display:flex;align-items:center;justify-content:center;clip-path:polygon(0 0,85% 0,100% 100%,15% 100%)}
.deal{top:1570px;width:246px;height:295px;overflow:hidden;box-shadow:0 14px 20px rgba(0,0,0,.18)}
.deal-img{position:absolute;inset:0}
.deal-tag{position:absolute;left:0;bottom:0;width:100%;height:80px}
.deal-icon{position:absolute;left:0;bottom:0;width:110px;height:80px;background:#fff;clip-path:polygon(0 0,70% 0,100% 100%,0 100%)}
.deal-icon i{position:absolute;left:14px;top:24px;width:36px;height:28px;border:4px solid var(--gold);border-radius:4px}
.deal-name{position:absolute;left:115px;bottom:24px;color:#fff;font-size:21px;font-weight:600;white-space:nowrap}
.customs{top:1972px;left:0;width:1200px;height:513px;background:var(--light);overflow:hidden}
.provide{top:3175px;width:330px;height:385px;background:#fff;box-shadow:0 6px 18px rgba(0,0,0,.08)}
.provide .ph{height:270px}
.provide h3{margin:32px 0 0 34px;font-size:19px;font-weight:600;letter-spacing:.5px;white-space:nowrap}
.provide p{margin:4px 34px 0 34px;font-family:"Roboto",sans-serif;font-size:13px;color:#555;line-height:18px}
.stores{left:300px;top:3748px;width:600px;display:flex;justify-content:space-between;align-items:center}
.store{width:140px;text-align:center;font-size:22px;font-weight:700;color:var(--navy);white-space:nowrap}
.footer{top:3800px;left:0;width:1200px;height:530px}
.flinks{display:flex;gap:34px;justify-content:center;color:#fff;font-size:14px}
.fsoc{display:flex;gap:12px;justify-content:center}
.fsoc span{width:34px;height:34px;border-radius:50%;border:1px solid rgba(255,255,255,.5);color:#fff;font-size:9px;display:flex;align-items:center;justify-content:center}
</style>
</head>
<body>

<header>
  <div class="abs brand" style="left:88px;top:24px"><span class="brand-dot"></span>MAR-WICK SKY HARBOR</div>
  <div class="abs social" style="left:730px;top:32px"><span>Folio</span><span>Chirp</span><span>Circleup</span><span>Worklink</span></div>
  <svg class="abs" style="left:968px;top:24px" width="26" height="26" viewBox="0 0 24 24"><path fill="#e9a800" d="M6.6 10.8c1.4 2.8 3.8 5.1 6.6 6.6l2.2-2.2c.3-.3.7-.4 1-.2 1.1.4 2.3.6 3.6.6.6 0 1 .4 1 1V20c0 .6-.4 1-1 1C10.6 21 3 13.4 3 4c0-.6.4-1 1-1h3.5c.6 0 1 .4 1 1 0 1.3.2 2.5.6 3.6.1.3 0 .7-.2 1z"/></svg>
  <div class="abs" style="left:1004px;top:20px;font-size:10px;color:#333">TELEPHONE:</div>
  <div class="abs" style="left:1004px;top:32px;font-size:14px;font-weight:700;color:#222;white-space:nowrap">(876)555-0193</div>
</header>

<nav class="abs nav">
  <ul>
    <li class="active">HOME</li><li>ABOUT US</li><li>SERVICES</li><li>SHIPPING CALCULATOR</li><li>CONTACT</li><li>FORMS</li><li>REGISTER</li><li>LOGIN</li>
  </ul>
  <svg class="abs" style="left:1086px;top:12px" width="20" height="18" viewBox="0 0 20 18"><path fill="#fff" d="M0 1h3l3 10h10l3-8H5" stroke="#fff" stroke-width="1.5"/><circle cx="7" cy="15" r="1.8" fill="#fff"/><circle cx="15" cy="15" r="1.8" fill="#fff"/></svg>
</nav>

<section class="abs hero">
  <div class="hero-photo" role="img" aria-label="Smiling delivery worker in a yellow shirt and blue overalls carrying a cardboard box beside a white van"></div>
  <div class="abs hero-kicker">CREATING WAVES IN THE</div>
  <div class="abs hero-title">LOGISTIC<br>INDUSTRY.</div>
  <div class="abs arrow" style="left:0;top:304px">‹</div>
  <div class="abs arrow" style="right:0;top:304px">›</div>
  <div class="abs" style="left:591px;top:624px;width:18px;height:28px;border:2px solid #fff;border-radius:9px"></div>
  <svg class="abs" style="left:0;top:0" width="1200" height="830" viewBox="0 0 1200 830">
    <path fill="#e9a800" d="M0 470 C80 720 300 780 500 760 C700 740 850 700 1010 760 C1100 790 1170 810 1200 828 L1200 830 L0 830Z"/>
    <path fill="#fff" d="M0 560 C120 790 320 800 520 776 C720 752 860 740 1020 790 C1110 815 1170 825 1200 830 L0 830Z"/>
  </svg>
</section>

<section>
  <div class="abs" style="left:88px;top:1255px;width:264px;height:182px;border:14px solid var(--gold)"></div>
  <div class="abs" role="img" aria-label="Delivery driver in cap and yellow shirt at the wheel of a van" style="left:150px;top:945px;width:372px;height:433px;background:linear-gradient(135deg,#5d7fa3,#c7c9c6 55%,#e8c25a);box-shadow:0 10px 25px rgba(0,0,0,.15)"></div>
  <h2 class="abs sec" style="left:624px;top:1070px">ABOUT US</h2>
  <p class="abs body" style="left:624px;top:1122px;width:482px">Lorem Ipsum is simply dummy text of the printing and typesetting industry. Lorem Ipsum has been the industry's standard dummy text ever since the 1500s, when an unknown printer took a galley of type and scrambled it to make a type specimen book. It has survived not only five centuries, but also the leap .</p>
  <div class="abs btn-slant" style="left:624px;top:1268px;width:146px">READ MORE</div>
</section>

<section>
  <h2 class="abs sec center" style="top:1503px">COMPANY DEALS</h2>
  <div class="abs deal" style="left:88px"><div class="deal-img" role="img" aria-label="Container ship at a port with cranes" style="background:linear-gradient(180deg,#9fb5cc,#6b7f96 50%,#2f4a6a)"></div><div class="deal-tag"><div class="deal-icon"><i></i></div><div class="deal-name">Shipping</div></div></div>
  <div class="abs deal" style="left:347px"><div class="deal-img" role="img" aria-label="Worker with clipboard among stacked shipping containers" style="background:linear-gradient(180deg,#3d5f8c,#a4523a 55%,#2a3c56)"></div><div class="deal-tag"><div class="deal-icon"><i></i></div><div class="deal-name">Logistic</div></div></div>
  <div class="abs deal" style="left:606px"><div class="deal-img" role="img" aria-label="Forklift lifting a container at a sunset terminal" style="background:linear-gradient(180deg,#e3c08a,#d89a55 50%,#3b5b86)"></div><div class="deal-tag"><div class="deal-icon"><i></i></div><div class="deal-name">Imports</div></div></div>
  <div class="abs deal" style="left:865px"><div class="deal-img" role="img" aria-label="Cargo truck and worker with a plane overhead" style="background:linear-gradient(180deg,#f0b56a,#b98c66 50%,#3b4a5e)"></div><div class="deal-tag"><div class="deal-icon"><i style="border-radius:50%;width:32px;height:32px"></i></div><div class="deal-name">Export</div></div></div>
</section>

<section class="abs customs">
  <svg class="abs" style="left:0;top:0" width="1200" height="513" viewBox="0 0 1200 513"><path fill="#0f3a6e" d="M745 0 H1200 V513 H880Z"/><rect x="720" y="78" width="10" height="22" fill="#e9a800" transform="rotate(20 725 89)"/><rect x="830" y="430" width="10" height="22" fill="#e9a800" transform="rotate(-20 835 441)"/></svg>
  <div class="abs" role="img" aria-label="Two smiling warehouse staff leaning over a desk between shelving aisles" style="left:560px;top:96px;width:508px;height:342px;background:linear-gradient(135deg,#3f6388,#c9b48f 50%,#7e8a99);clip-path:polygon(0 0,100% 0,100% 100%,10% 100%)"></div>
  <h2 class="abs sec" style="left:85px;top:190px;white-space:nowrap">CUSTOMS CLEARANCE</h2>
  <p class="abs body" style="left:86px;top:240px;width:432px;font-size:15px;line-height:24px;color:#444">Customs broker services andcustomers can shop online and we take care of the shipment from the United States of America to Jamaica.</p>
  <div class="abs" style="left:84px;top:330px;width:146px;height:34px;clip-path:polygon(0 0,85% 0,100% 100%,15% 100%);background:var(--gold)"><div style="position:absolute;inset:2px 3px;clip-path:polygon(0 0,85% 0,100% 100%,15% 100%);background:var(--light);display:flex;align-items:center;justify-content:center;font-size:11px;font-weight:700">CONTACT US</div></div>
</section>

<section>
  <div class="abs" role="img" aria-label="Running courier in blue shirt carrying parcels in front of a globe swoosh" style="left:85px;top:2440px;width:525px;height:590px;background:radial-gradient(ellipse at 55% 45%,#2b6cc4 0%,#5f88bf 30%,#e6ebf2 62%,#fff 75%)"></div>
  <h2 class="abs sec" style="left:697px;top:2626px;font-size:36px;white-space:nowrap">SHIPPING WEIGHT<br>CALCULATOR</h2>
  <div class="abs" style="left:697px;top:2735px;width:375px;height:50px;background:#eee"></div>
  <div class="abs" style="left:697px;top:2805px;font-size:21px;line-height:27px;color:#222;width:340px">Estimated freight cost/courier fee is: <b>$: 0 USD.</b></div>
  <div class="abs" style="left:700px;top:2867px;font-family:Roboto,sans-serif;font-size:13.5px;line-height:24px;color:#444;width:380px">(Based on weight of package only)<br>Packages over $ 50.00 usd in value are subjected to Custom charges.<br>Please contact one of our offices for further details.</div>
</section>

<section>
  <h2 class="abs sec center" style="top:3075px">WHAT WE PROVIDE<br>FOR CLIENTS</h2>
  <div class="abs provide" style="left:88px"><div class="ph" role="img" aria-label="Woman packing a parcel at a desk" style="background:linear-gradient(135deg,#d8b07a,#3e6aa0 60%,#e9e4dc)"></div><h3>IN STORE PICKUP</h3><p>Stores open until 6 PM*</p></div>
  <div class="abs provide" style="left:435px"><div class="ph" role="img" aria-label="Woman with clipboard in a warehouse aisle" style="background:linear-gradient(135deg,#3d6597,#d6c6a6 50%,#8aa0bd)"></div><h3>IN STORE PURCHASING</h3><p>Credit card services and knowledgeable shopping assistant</p></div>
  <div class="abs provide" style="left:782px"><div class="ph" role="img" aria-label="Courier in orange shirt driving a delivery van" style="background:linear-gradient(135deg,#4d5c70,#e9a94a 55%,#f0eee9)"></div><h3>BUSINESS DELIVERY</h3><p>FREE DELIVERY to Kingston business addresses!</p></div>
</section>

<section>
  <h2 class="abs sec center" style="top:3662px">ONLINE STORES</h2>
  <div class="abs stores">
    <span class="store">Amberly</span><span class="store">Top Deal Hub</span><span class="store">Bidloop</span><span class="store">Valuemart</span>
  </div>
</section>

<footer class="abs footer">
  <svg class="abs" style="left:0;top:0" width="1200" height="530" viewBox="0 0 1200 530">
    <path fill="#0f3a6e" d="M0 15 C150 110 350 90 550 60 C750 30 900 40 1040 110 C1120 150 1180 220 1200 270 V530 H0Z"/>
    <path fill="#e9a800" d="M700 40 C860 30 1000 60 1090 140 C1150 190 1190 240 1200 280 L1200 300 C1170 240 1120 180 1060 140 C960 80 840 50 700 40Z"/>
  </svg>
  <div class="abs center" style="top:195px;display:flex;justify-content:center;align-items:center;gap:10px;color:#fff;font-size:26px;font-weight:700;letter-spacing:1px;white-space:nowrap"><span style="width:26px;height:26px;border-radius:50%;background:#fff"></span>MAR-WICK SKY HARBOR</div>
  <div class="abs center" style="top:240px;color:#cfd8e6;font-size:14px;letter-spacing:6px">Custom Brokers Ltd.</div>
  <div class="abs center flinks" style="top:343px"><span>Home</span><span>Contact</span><span>Terms &amp; Condition</span><span>Shipping Calculator</span></div>
  <div class="abs center fsoc" style="top:380px"><span>Fo</span><span>Ch</span><span>Ci</span><span>Wo</span></div>
  <div class="abs" style="left:88px;top:480px;width:1024px;height:1px;background:rgba(255,255,255,.2)"></div>
  <div class="abs center" style="top:496px;color:#fff;font-size:13px">Copyright 2020 | All Rights Reserved</div>
  <div class="abs" style="left:1139px;top:456px;width:34px;height:34px;border-radius:50%;background:var(--gold);color:#fff;font-size:12px;display:flex;align-items:center;justify-content:center">^</div>
</footer>

</body>
</html>
```